Honey Packaging Label Design

The honey packaging label should be designed in a transparent look. The design concept for this product should be natural and healthy. Please include the logo and nutrition fact in the attachment. The size for the label is 9cm width by 5cm height. Please also include the information of our company. Since the bar code is not ready yet, please leave space for the bar code.
Velmora International Trading Group Inc.
#2487 - 736 Thistlebrook St., Vancouver, V5K 2R8
Tel: 1-604-820-3147/3146
Since our company's logo for the packaging is still not finished yet, so please leave space for our logo, and we will be able to add it on later.

Please be creative.

If you have any question you can call at 1-604-820-3147/3146 or e-mail to marthak@velmora-example.ca

Thank you!

Target Market(s)

Supermarket, wholesale

Industry/Entity Type

Product

Requirements
Must have
• Nutrition facts, bar code, logo, address, transparent, modern look design, geometry design.
Nice to have
• Bees, flowers
Should not have
• Traditional design.

```html
<!DOCTYPE html>
<html lang="en">
<head>
<meta charset="utf-8">
<title>Honey Label – Canadian White Honey</title>
<link rel="stylesheet" href="https://fonts.googleapis.com/css2?family=Jost:wght@400;500;600&family=Oswald:wght@300;400;500&display=swap">
<style>
  :root {
    --page: #e9e9e9;
    --label: #efefef;
    --brown: #4a2610;
    --gold: #f6a623;
    --white: #ffffff;
  }
  html, body {
    margin: 0;
    width: 1200px;
    height: 921px;
    overflow: hidden;
    background: var(--page);
  }
  .label {
    position: absolute;
    left: 50px;
    top: 165px;
    width: 1100px;
    height: 590px;
    display: block;
  }
  .brand-name { font-family: "Jost", sans-serif; font-weight: 500; }
  .brand-sub { font-family: "Jost", sans-serif; font-weight: 400; }
  .info { font-family: "Oswald", sans-serif; }
  .company-logo { font-family: "Jost", sans-serif; font-weight: 600; }
</style>
</head>
<body>
<svg class="label" viewBox="0 0 388 208" xmlns="http://www.w3.org/2000/svg">
  <defs>
    <clipPath id="label-edge"><rect width="388" height="208"/></clipPath>
  </defs>

  <rect class="label-base" width="388" height="208" fill="var(--label)"/>

  <g clip-path="url(#label-edge)">
    <!-- front hexagon -->
    <polygon class="hex-front" points="58,0 192,0 240,95 185,208 65,208 10,95"
             fill="var(--brown)" stroke="var(--brown)" stroke-width="10" stroke-linejoin="round"/>
    <!-- side panel hexagon -->
    <polygon class="hex-side" points="292,0 400,0 400,208 262,208 196,104"
             fill="var(--brown)" stroke="var(--brown)" stroke-width="10" stroke-linejoin="round"/>

    <!-- striped gaps forming the lower honeycomb -->
    <g class="stripe-gaps" fill="var(--label)">
      <polygon points="0,119 244,119 252,137 0,137"/>
      <polygon points="0,147 257,147 268,166 0,166"/>
      <polygon points="0,176 273,176 281,190 0,190"/>
      <polygon points="0,202 288,202 292,210 0,210"/>
    </g>
  </g>

  <!-- product brand -->
  <circle class="brand-mark" cx="124" cy="32" r="9" fill="var(--gold)"/>
  <text class="brand-name" x="124" y="83" text-anchor="middle" font-size="34" fill="var(--white)" letter-spacing="1">HONEY</text>
  <g class="brand-dots" fill="var(--gold)">
    <circle cx="68" cy="94" r="1.3"/><circle cx="72" cy="94" r="1.3"/><circle cx="76" cy="94" r="1.3"/>
    <circle cx="172" cy="94" r="1.3"/><circle cx="176" cy="94" r="1.3"/><circle cx="180" cy="94" r="1.3"/>
  </g>
  <text class="brand-sub" x="124" y="96" text-anchor="middle" font-size="6" fill="var(--white)">Canadian White Honey</text>

  <!-- company information -->
  <text class="info company-line" x="38" y="130" font-size="5.6" fill="var(--gold)" font-weight="500">Velmora International Trading Group Inc. #2487 - 736 Thistlebrook St.,</text>
  <text class="info company-line" x="62" y="159" font-size="5.6" fill="var(--gold)" font-weight="500">Vancouver, V5K 2R8  Tel: 1-604-820-3147/3146</text>

  <!-- logo placeholder -->
  <text class="company-logo" x="379" y="20" text-anchor="end" font-size="8" fill="var(--white)">COMPANY</text>
  <text class="company-logo" x="373" y="31" text-anchor="end" font-size="8" fill="var(--white)">LOGO</text>

  <!-- nutrition facts -->
  <g class="info nutrition" text-anchor="end">
    <text x="381" y="47" font-size="5.4" font-weight="500" fill="var(--gold)">Nutrition Fact / Valeur nutritive</text>
    <text x="385" y="55" font-size="3.6" fill="var(--gold)">Per 1 tablespoon (20 g) / Pour 1 cuillère à table (20 g)</text>
    <g font-size="4.4" font-weight="300" fill="var(--white)">
      <text x="334" y="70">Amount - % Daily Values</text>
      <text x="334" y="77">Teneur - % valeur quotidienne</text>
      <text x="334" y="84">Calories / Calories 60</text>
      <text x="334" y="91">Fat / Lipides 0 g - 0 %</text>
      <text x="334" y="98">Carbohydrate / Glucides 17 g - 6 %</text>
      <text x="334" y="105">Sugars / Sucres 16 g</text>
      <text x="334" y="112">Protein / Protéines 0 g</text>
    </g>
    <g font-size="3.9" font-weight="300" fill="var(--white)">
      <text x="378" y="143">NOT A SIGNIFICANT SOURCE OF SATURATED FAT, TRANS</text>
      <text x="378" y="150">FAT, CHOLESTEROL, SODIUM, FIBRE, VITAMIN A,</text>
      <text x="378" y="157">VITAMIN C, CALCIUM OR IRON. / SOURCE</text>
      <text x="378" y="164">NÉGLIGEABLE DE LIPIDES SATURÉS, LIPIDES TRANS,</text>
      <text x="378" y="171">CHOLESTÉROL, SODIUM, FIBRES, VITAMINE A,</text>
      <text x="378" y="178">VITAMINE C, CALCIUM ET FER.</text>
    </g>
  </g>

  <!-- bar code space -->
  <rect class="barcode-space" x="340" y="76" width="48" height="55" fill="var(--gold)"/>
  <text class="company-logo" transform="translate(366 104) rotate(-90)" text-anchor="middle" font-size="7" fill="var(--brown)">BAR CODE</text>
</svg>
</body>
</html>
```